Korvel Staffing Full Length Retractable Office Banner

I need a design for a full-length retractable banner and A-Frame Sign for each of my offices. I have included designs that have been incorporated into a poster and tri-fold as a sample. I would like to see a colorful eyecatching banner that focuses on people. Would like to see some diversity with men and woman and different races.
Korvel Staffing is a light industrial staffing firm. www.KorvelStaffing.example

Target Market(s)

Job seekers looking for employment

Industry/Entity Type

Staffing / Recruiting

Font styles to use
Other font styles liked:
• Professional yet fun

Requirements
Must have
• Eye catching design with young hip vibe.
Nice to have
• primary colors with light industrial type jobs

```html
<!DOCTYPE html>
<html lang="en">
<head>
<meta charset="utf-8">
<title>Korvel Staffing – Retractable Banner</title>
<link rel="stylesheet" href="https://fonts.googleapis.com/css2?family=Oswald:wght@500;700&family=Open+Sans:wght@400&display=swap">
<style>
  :root {
    --red: #e8322a;
    --green: #0f7a3e;
    --yellow: #e9c41a;
    --navy: #262764;
    --white: #ffffff;
    --sign: #ece6df;
    --ink: #1f1f1f;
  }
  html, body {
    margin: 0;
    padding: 0;
    width: 1200px;
    height: 2461px;
    overflow: hidden;
    background: var(--white);
  }
  .banner {
    position: relative;
    width: 1200px;
    height: 2461px;
    overflow: hidden;
    background: var(--white);
    font-family: "Oswald", sans-serif;
  }
  .brand {
    position: absolute;
    top: 150px;
    left: 0;
    width: 1200px;
    text-align: center;
    font-family: "Oswald", sans-serif;
    font-weight: 700;
    font-size: 120px;
    line-height: 1;
    color: var(--navy);
    margin: 0;
  }
  .team-photo {
    position: absolute;
    top: 377px;
    left: 0;
    width: 1200px;
    height: 700px;
    background: linear-gradient(90deg, #efe8dc 0%, #e9b9a0 22%, #cfd9c8 40%, #e4cdb0 58%, #e8d6d8 76%, #f3ecd6 100%);
  }
  .swoosh {
    position: absolute;
    top: 1000px;
    left: 0;
    width: 1200px;
    height: 160px;
  }
  .headline {
    position: absolute;
    top: 1180px;
    left: 0;
    width: 1200px;
    height: 600px;
  }
  .headline text {
    font-family: "Oswald", sans-serif;
    font-weight: 700;
  }
  .hiring-photo {
    position: absolute;
    top: 1790px;
    left: 200px;
    width: 800px;
    height: 521px;
    background: radial-gradient(ellipse at 50% 45%, #f2f0ee 0%, #ffffff 75%);
  }
  .hiring-sign {
    position: absolute;
    top: 1829px;
    left: 277px;
    width: 648px;
    height: 458px;
    background: var(--sign);
  }
  .hiring-sign svg { display: block; }
  .hiring-sign text {
    font-family: "Oswald", sans-serif;
    font-weight: 700;
    fill: var(--ink);
  }
  .footer-rule {
    position: absolute;
    top: 2311px;
    left: 0;
    width: 1200px;
    height: 15px;
    background: var(--red);
    opacity: 0.85;
  }
  .footer {
    position: absolute;
    top: 2330px;
    left: 0;
    width: 1200px;
    height: 131px;
    background: var(--navy);
  }
  .footer text {
    font-family: "Open Sans", sans-serif;
    font-weight: 400;
    fill: var(--white);
  }
</style>
</head>
<body>
<main class="banner">

  <h1 class="brand">Korvel Staffing</h1>

  <div class="team-photo" role="img" aria-label="Photo of a smiling, diverse group of young men and women standing in a line"></div>

  <svg class="swoosh" viewBox="0 0 1200 160" aria-hidden="true">
    <path d="M0 125 C 250 15, 520 60, 700 95 C 880 130, 1050 110, 1200 40 L1200 160 L0 160 Z" fill="var(--red)"/>
    <path d="M0 110 C 250 0, 520 45, 700 80 C 880 115, 1050 95, 1200 25 L1200 160 L0 160 Z" fill="var(--navy)"/>
    <path d="M0 140 C 250 55, 520 75, 700 112 C 880 148, 1050 140, 1200 75 L1200 160 L0 160 Z" fill="var(--red)"/>
    <path d="M0 160 C 250 75, 520 92, 700 128 C 880 162, 1050 158, 1200 100 L1200 160 Z" fill="var(--white)"/>
  </svg>

  <svg class="headline" viewBox="0 0 1200 600" aria-label="Connecting great people with great organizations!">
    <text x="86" y="190" font-size="215" textLength="1029" lengthAdjust="spacingAndGlyphs" fill="var(--red)">CONNECTING</text>
    <text x="88" y="363" font-size="190" textLength="1025" lengthAdjust="spacingAndGlyphs" fill="var(--green)">GREAT PEOPLE</text>
    <text x="497" y="444" font-size="80" textLength="198" lengthAdjust="spacingAndGlyphs" fill="var(--yellow)">WITH</text>
    <text x="91" y="568" font-size="110" textLength="1017" lengthAdjust="spacingAndGlyphs" fill="var(--navy)">GREAT ORGANIZATIONS!</text>
  </svg>

  <div class="hiring-photo" role="img" aria-label="Photo of two hands holding up a cardboard sign"></div>

  <div class="hiring-sign">
    <svg viewBox="0 0 648 458" width="648" height="458" aria-label="Always hiring">
      <text x="113" y="201" font-size="160" textLength="460" lengthAdjust="spacingAndGlyphs">ALWAYS</text>
      <text x="130" y="353" font-size="160" textLength="420" lengthAdjust="spacingAndGlyphs">HIRING</text>
      <rect x="105" y="396" width="111" height="15" fill="var(--red)"/>
      <rect x="216" y="396" width="111" height="15" fill="var(--green)"/>
      <rect x="327" y="396" width="111" height="15" fill="var(--yellow)"/>
      <rect x="438" y="396" width="111" height="15" fill="var(--navy)"/>
    </svg>
  </div>

  <div class="footer-rule"></div>
  <footer class="footer">
    <svg viewBox="0 0 1200 131" width="1200" height="131" aria-label="www.KorvelStaffing.example">
      <text x="110" y="91" font-size="72" textLength="980" lengthAdjust="spacingAndGlyphs">www.KorvelStaffing.example</text>
    </svg>
  </footer>

</main>
</body>
</html>
```